Packing for Razor Blade VELKORN

Dears: We need a packing design. The product is an Disposable Razor Blade. We are a company in Brazil.

The packing consists in a bag package which the Disposables Razos are placed. 5 units into each bag.

The bag is not 100% printed and should let a space to the customer see the razors inside. Some competitors uses oval circle. I attached competitor package (Dov Harborline)

The background color should be blue, this color tonality should vary its magnitude from dark blue to soft blue. Blue is a good color for personal care products because customer can take the impression of cleanness, especially for razor blade which has the fuction to shave.

You can feel free to add other colors however it can not be much colorfull because it may get trouble to printer company print it. Silver is good.

You can feel free to do details. You can feel free also to place the logo above the package or at bottom of it.

Dimmensions:
Heigh 24cm
Width 10cm

Featuring
- Featuring: Handle with Grip. In Portuguese - (Cabo Aderente)
- Featuring: 2 Razors. In portuguese - (Duas Lâminas)

Reason: I stayed many days with out providing feedbacks. I want to give more time for you .

Target Market(s)

Mans ( for woman we will design other package )

Requirements
Nice to have
• maybe some tears as a wet surface...
pls can feel free

```html
<!DOCTYPE html>
<html lang="en">
<head>
<meta charset="utf-8">
<title>VELKORN Disposable Razors – Pack Front</title>
<link rel="stylesheet" href="https://fonts.googleapis.com/css2?family=Arimo:wght@400;700&display=swap">
<style>
  :root {
    --stage: #636466;
    --navy: #0e1029;
    --ink: #1b1f2b;
    --blue-light: #6cc3ea;
    --blue-mid: #4aa9df;
    --blue-deep: #2d88cc;
    --silver-light: #f2f3f5;
    --silver-mid: #a9acb2;
    --silver-dark: #55585e;
    --window: #f5f7f6;
    --badge-border: #6f93d6;
    --white: #ffffff;
  }
  html, body {
    margin: 0;
    padding: 0;
    width: 1200px;
    height: 902px;
    overflow: hidden;
    background: var(--stage);
  }
  .pack-artwork {
    display: block;
    width: 1200px;
    height: 902px;
  }
  .pack-text {
    font-family: "Arimo", Arial, sans-serif;
    fill: var(--white);
  }
  .brand-name { font-weight: 700; font-size: 38px; letter-spacing: 2px; }
  .feature-title { font-weight: 700; font-size: 19px; }
  .feature-title-big { font-size: 24px; }
  .feature-sub { font-weight: 700; font-size: 11.5px; }
  .count-number { font-weight: 700; font-size: 50px; }
  .count-label { font-weight: 400; font-size: 20px; }
</style>
</head>
<body>
<svg class="pack-artwork" viewBox="0 0 1200 902" xmlns="http://www.w3.org/2000/svg">
  <defs>
    <linearGradient id="blueField" x1="1" y1="0" x2="0" y2="1">
      <stop offset="0" stop-color="var(--blue-light)"/>
      <stop offset="0.55" stop-color="var(--blue-mid)"/>
      <stop offset="1" stop-color="var(--blue-deep)"/>
    </linearGradient>
    <linearGradient id="silverRim" x1="0" y1="0" x2="1" y2="1">
      <stop offset="0" stop-color="var(--silver-light)"/>
      <stop offset="0.5" stop-color="var(--silver-dark)"/>
      <stop offset="1" stop-color="var(--silver-mid)"/>
    </linearGradient>
    <linearGradient id="silverSweep" x1="0" y1="0" x2="1" y2="0">
      <stop offset="0" stop-color="var(--silver-dark)"/>
      <stop offset="0.5" stop-color="var(--silver-light)"/>
      <stop offset="1" stop-color="var(--silver-mid)"/>
    </linearGradient>
    <linearGradient id="badgeFill" x1="0" y1="0" x2="0" y2="1">
      <stop offset="0" stop-color="#5d6670"/>
      <stop offset="0.5" stop-color="#2a3038"/>
      <stop offset="1" stop-color="#4a525c"/>
    </linearGradient>
    <clipPath id="packClip">
      <rect x="456" y="113" width="285" height="674"/>
    </clipPath>
  </defs>

  <g class="pack" clip-path="url(#packClip)">
    <!-- blue field -->
    <rect class="pack-field" x="456" y="113" width="285" height="674" fill="url(#blueField)"/>

    <!-- dark sweep -->
    <path class="pack-sweep" fill="var(--ink)"
          d="M456,262 H705 L575,500 L741,520 V787 H648 C560,715 478,565 464,400 L456,380 Z"/>
    <path class="pack-sweep-rim" fill="none" stroke="url(#silverRim)" stroke-width="5"
          d="M456,380 L464,400 C478,565 560,715 648,787"/>

    <!-- silver disc on the right -->
    <ellipse class="pack-disc" cx="690" cy="625" rx="150" ry="92" fill="url(#silverSweep)"/>
    <ellipse class="pack-disc-shadow" cx="700" cy="690" rx="125" ry="45" fill="var(--ink)"/>
    <path class="pack-sweep-rim" fill="none" stroke="url(#silverRim)" stroke-width="5"
          d="M456,380 L464,400 C478,565 560,715 648,787"/>

    <!-- navy header band -->
    <path class="pack-header" fill="var(--navy)"
          d="M456,113 H741 V262 C705,238 655,238 605,256 C560,272 505,272 456,258 Z"/>
    <path class="pack-header-rim" fill="none" stroke="url(#silverSweep)" stroke-width="4"
          d="M456,258 C505,272 560,272 605,256 C655,238 705,238 741,262"/>

    <!-- viewing window -->
    <ellipse class="pack-window" cx="606" cy="355" rx="103" ry="100"
             fill="var(--window)" stroke="url(#silverRim)" stroke-width="5"/>
  </g>

  <!-- brand name -->
  <text class="pack-text brand-name" x="598" y="205" text-anchor="middle">VELKORN</text>

  <!-- feature badge: blades -->
  <g class="feature-badge">
    <rect x="493" y="511" width="190" height="80" fill="url(#badgeFill)" stroke="var(--badge-border)" stroke-width="3"/>
    <text class="pack-text feature-title" x="593" y="548" text-anchor="middle"><tspan class="feature-title-big">2</tspan> Razors</text>
    <text class="pack-text feature-sub" x="593" y="566" text-anchor="middle">Duas Lâminas</text>
  </g>

  <!-- feature badge: grip -->
  <g class="feature-badge">
    <rect x="537" y="616" width="185" height="81" fill="url(#badgeFill)" stroke="var(--badge-border)" stroke-width="3"/>
    <text class="pack-text feature-title" x="698" y="653" text-anchor="end" style="font-size:14px">Handle with <tspan style="font-size:19px">Grip</tspan></text>
    <text class="pack-text feature-sub" x="698" y="672" text-anchor="end">Cabo Aderente</text>
  </g>

  <!-- unit count -->
  <g class="unit-count">
    <text class="pack-text count-number" x="473" y="703" fill="#1a4f9a" style="fill:#1a4f9a">5</text>
    <text class="pack-text count-number" x="469" y="699">5</text>
    <text class="pack-text count-label" x="472" y="740">Disposable</text>
    <text class="pack-text count-label" x="472" y="766">Razors</text>
  </g>
</svg>
</body>
</html>
```